Business cards design on a high standard

We advise clients on insurance and financial matters, since these clients pay for our advice, the design should have a high standard. Our logo should be included. From the colors we are open for everything.

Colors

Designer to choose colors to be used in the design.

```html
<!DOCTYPE html>
<html lang="en">
<head>
<meta charset="utf-8">
<title>Alpine Counsel – Business Cards</title>
<link href="https://fonts.googleapis.com/css2?family=Michroma&family=Nunito+Sans:wght@400;700&display=swap" rel="stylesheet">
<style>
  :root {
    --backdrop: #2b2b2d;
    --card: #1d1d1f;
    --red: #e0242b;
    --grey: #a7a7ab;
    --text: #cfcfd2;
  }
  * { margin: 0; padding: 0; box-sizing: border-box; }
  html, body { width: 1200px; height: 900px; overflow: hidden; }
  body {
    background: var(--backdrop);
    font-family: "Nunito Sans", Arial, sans-serif;
    position: relative;
  }
  .card {
    position: absolute;
    left: 250px;
    width: 700px;
    height: 400px;
    background: var(--card);
    box-shadow: 0 12px 30px rgba(0,0,0,.55);
    overflow: hidden;
  }
  .card--front { top: 38px; }
  .card--back { top: 462px; }

  .brand {
    display: flex;
    align-items: center;
    gap: 14px;
    font-family: "Michroma", Arial, sans-serif;
    color: var(--red);
    letter-spacing: 2px;
    white-space: nowrap;
  }
  .brand__dot {
    width: 14px; height: 14px;
    border-radius: 50%;
    background: var(--grey);
  }
  .card--front .brand {
    position: absolute;
    left: 50%; top: 50%;
    transform: translate(-50%, -50%);
    font-size: 34px;
  }
  .card--back .brand {
    position: absolute;
    right: 40px; top: 70px;
    font-size: 28px;
  }

  .person { position: absolute; left: 330px; top: 150px; }
  .person__name {
    font-family: "Michroma", Arial, sans-serif;
    color: var(--red);
    font-size: 19px;
    letter-spacing: 4px;
  }
  .person__role { color: var(--text); font-size: 16px; margin-top: 2px; }

  .divider {
    position: absolute;
    left: 330px; right: 20px; top: 236px;
    height: 1.5px;
    background: var(--red);
  }

  .contacts {
    position: absolute;
    left: 330px; top: 258px;
    list-style: none;
  }
  .contacts li {
    display: flex;
    align-items: center;
    gap: 12px;
    color: var(--text);
    font-size: 17px;
    height: 30px;
  }
  .contacts svg { width: 18px; height: 18px; flex: none; }
  .contacts strong { color: var(--red); font-weight: 700; }

  .bands { position: absolute; left: 0; bottom: 0; width: 700px; height: 40px; }
</style>
</head>
<body>
  <section class="card card--front">
    <div class="brand"><span class="brand__dot"></span>ALPINE COUNSEL</div>
  </section>

  <section class="card card--back">
    <div class="brand"><span class="brand__dot"></span>ALPINE COUNSEL</div>

    <div class="person">
      <div class="person__name">MARCO VENTURI</div>
      <div class="person__role">CEO &amp; Founder</div>
    </div>

    <div class="divider"></div>

    <ul class="contacts">
      <li>
        <svg viewBox="0 0 24 24" fill="none" stroke="#e0242b" stroke-width="1.8"><circle cx="12" cy="12" r="10"/><path d="M8.5 7.5c0 4.5 3.5 8 8 8l1-2-2.5-1.2-1 1c-1.5-.6-2.7-1.8-3.3-3.3l1-1L10.5 6.5z"/></svg>
        +34 600.218.475
      </li>
      <li>
        <svg viewBox="0 0 24 24" fill="none" stroke="#e0242b" stroke-width="1.8"><rect x="2" y="5" width="20" height="14"/><path d="M2 5l10 8 10-8"/></svg>
        venturi@alpinecounsel.com
      </li>
      <li>
        <svg viewBox="0 0 24 24" fill="none" stroke="#e0242b" stroke-width="1.8"><circle cx="12" cy="12" r="10"/><path d="M2 12h20M12 2c3 3 3 17 0 20M12 2c-3 3-3 17 0 20"/></svg>
        <span>www.<strong>alpinecounsel</strong>.com</span>
      </li>
    </ul>

    <svg class="bands" viewBox="0 0 700 40" preserveAspectRatio="none">
      <polygon points="0,30 318,30 326,40 0,40" fill="#a7a7ab"/>
      <polygon points="300,2 700,2 700,40 326,40" fill="#e0242b"/>
    </svg>
  </section>
</body>
</html>
```